One Page Sales Flyer for Wireless Survey- Computer Hardware

I want a designer to create a one page 4 color sales slick to be given to our sales team to sell to the end customers. I would like a visual picture of a heat map so vornix "heat map wireless" to get an idea of how that image should look.

```html
<!DOCTYPE html>
<html lang="en">
<head>
<meta charset="utf-8">
<title>Ardent – Wireless Site Surveys</title>
<link href="https://fonts.googleapis.com/css2?family=Montserrat:wght@400;500;600;700;800&family=Exo+2:wght@600;700&display=swap" rel="stylesheet">
<style>
  :root {
    --sky: #05a6e4;
    --headline: #1da2e0;
    --teal: #007ea1;
    --steel: #4a89ad;
    --navy: #0d4ea3;
    --ink: #1b1b1b;
    --white: #ffffff;
  }
  html, body {
    margin: 0;
    padding: 0;
    width: 1013px;
    height: 1200px;
    overflow: hidden;
    background: var(--white);
  }
  .flyer {
    position: relative;
    width: 1013px;
    height: 1200px;
    font-family: "Montserrat", sans-serif;
    color: var(--ink);
  }
  .flyer-shapes {
    position: absolute;
    inset: 0;
  }
  .brand {
    position: absolute;
    left: 48px;
    top: 40px;
    width: 236px;
    text-align: center;
  }
  .brand-square {
    display: block;
    width: 96px;
    height: 96px;
    margin: 0 auto 20px;
    border-radius: 12px;
    background: var(--sky);
  }
  .brand-name {
    font-weight: 500;
    font-size: 46px;
    letter-spacing: 1px;
    line-height: 1;
    color: var(--ink);
  }
  .headline {
    position: absolute;
    left: 48px;
    top: 306px;
    margin: 0;
    font-weight: 800;
    font-size: 40px;
    line-height: 45px;
    color: var(--headline);
    letter-spacing: 0.3px;
  }
  .section-title {
    position: absolute;
    left: 48px;
    margin: 0;
    font-weight: 700;
    font-size: 18px;
    color: var(--navy);
  }
  .section-text {
    position: absolute;
    left: 48px;
    margin: 0;
    font-size: 15px;
    line-height: 20px;
    text-align: justify;
    letter-spacing: -0.2px;
  }
  .benefits {
    position: absolute;
    left: 48px;
    top: 688px;
    width: 610px;
    margin: 0;
    padding: 0;
    list-style: none;
  }
  .benefit {
    position: relative;
    padding-left: 45px;
    font-size: 15px;
    line-height: 19px;
    text-align: justify;
    margin-bottom: 11px;
  }
  .benefit svg {
    position: absolute;
    left: 0;
    top: 3px;
  }
  .heat-map {
    position: absolute;
    inset: 0;
  }
  .targets {
    position: absolute;
    left: 709px;
    top: 586px;
    width: 290px;
  }
  .targets-title {
    margin: 0 0 16px;
    font-family: "Exo 2", sans-serif;
    font-weight: 700;
    font-size: 25px;
    color: var(--ink);
  }
  .targets-list {
    margin: 0;
    padding: 0;
    list-style: none;
  }
  .target {
    position: relative;
    padding-left: 31px;
    font-family: "Exo 2", sans-serif;
    font-weight: 700;
    font-size: 23px;
    line-height: 30px;
    color: var(--ink);
  }
  .target::before {
    content: "";
    position: absolute;
    left: 6px;
    top: 10px;
    width: 9px;
    height: 9px;
    border: 1.5px solid var(--ink);
  }
  .contact-title {
    position: absolute;
    left: 60px;
    top: 1034px;
    margin: 0;
    font-weight: 700;
    font-size: 37px;
    color: var(--white);
  }
  .phone {
    position: absolute;
    left: 57px;
    top: 1080px;
    display: flex;
    align-items: center;
    gap: 24px;
    font-family: "Exo 2", sans-serif;
    font-weight: 700;
    font-size: 62px;
    color: var(--white);
    letter-spacing: 1px;
  }
  .links {
    position: absolute;
    left: 614px;
    top: 1078px;
    margin: 0;
    padding: 0;
    list-style: none;
  }
  .link {
    display: flex;
    align-items: center;
    gap: 12px;
    font-weight: 600;
    font-size: 24px;
    line-height: 32px;
    color: var(--white);
  }
  .footnote {
    position: absolute;
    left: 53px;
    top: 1156px;
    margin: 0;
    font-size: 15px;
    color: var(--white);
  }
</style>
</head>
<body>
<main class="flyer">
  <svg class="flyer-shapes" width="1013" height="1200" viewBox="0 0 1013 1200" aria-hidden="true">
    <polygon points="345,0 704,0 704,201 345,281" fill="var(--sky)"/>
    <polygon points="704,0 1013,0 1013,209 704,281" fill="var(--teal)"/>
    <polyline points="0,281 345,201 345,281 704,201 704,281 1013,209" fill="none" stroke="var(--ink)" stroke-width="7" stroke-linejoin="miter"/>
    <polygon points="0,1040 682,891 682,1002 1013,1038 1013,1200 0,1200" fill="var(--sky)"/>
    <polygon points="0,906 424,947 0,1040" fill="var(--steel)"/>
    <polygon points="682,1002 1013,927 1013,1038" fill="#262626"/>
  </svg>

  <svg class="heat-map" width="1013" height="1200" viewBox="0 0 1013 1200" role="img" aria-label="Wireless signal heat map showing strong and weak coverage zones">
    <defs>
      <linearGradient id="heat-tones" x1="0" y1="0" x2="0.4" y2="1">
        <stop offset="0" stop-color="#f04d22"/>
        <stop offset="0.35" stop-color="#f5a318"/>
        <stop offset="0.6" stop-color="#f4e61c"/>
        <stop offset="0.85" stop-color="#8fd23a"/>
        <stop offset="1" stop-color="#f28a1f"/>
      </linearGradient>
    </defs>
    <polygon points="682,550 1013,486 1013,927 682,1002" fill="url(#heat-tones)"/>
  </svg>

  <div class="brand">
    <span class="brand-square"></span>
    <div class="brand-name">ARDENT</div>
  </div>

  <h1 class="headline">INCREASE HARDWARE AND SERVICES<br>SPEND WITH WIRELESS SITE SURVEYS</h1>

  <h2 class="section-title" style="top:412px">What is a wireless site survey or heat map?</h2>
  <p class="section-text" style="top:440px;width:917px">A wireless site survey is a compilation of reports showing a visual representation of health of your wireless network. This does not only show how strong or weak a wireless signal is in any location it also helps aid in channel and placement to ensure maximum stable data rates are archived even where the single appears strong.</p>

  <h2 class="section-title" style="top:520px">Why do customers need a site survey?</h2>
  <p class="section-text" style="top:546px;width:610px">Any variety of factors can contribute to an unhealthy wireless network (electrical, motors, materials used in construction, distance, neighboring wireless networks, etc.) and traditional methods that use only blueprints and a computer program to show signal strength have shown to be ineffective.</p>

  <h2 class="section-title" style="top:650px">Why should they use you?</h2>
  <ul class="benefits">
    <li class="benefit"><svg width="24" height="22" viewBox="0 0 24 22" aria-hidden="true"><circle cx="11" cy="11" r="9" fill="none" stroke="var(--sky)" stroke-width="2.2"/><polyline points="6,10 11,15 22,2" fill="none" stroke="var(--sky)" stroke-width="2.6"/></svg>42% of businesses report some issues with wireless connectivity and acknowledge its effect on the bottom line*</li>
    <li class="benefit"><svg width="24" height="22" viewBox="0 0 24 22" aria-hidden="true"><circle cx="11" cy="11" r="9" fill="none" stroke="var(--sky)" stroke-width="2.2"/><polyline points="6,10 11,15 22,2" fill="none" stroke="var(--sky)" stroke-width="2.6"/></svg>Most of these problems are solved through either fine tuning the current equipment (managed services) or purchasing new equipment (incremental sales) of which you can provide both</li>
    <li class="benefit"><svg width="24" height="22" viewBox="0 0 24 22" aria-hidden="true"><circle cx="11" cy="11" r="9" fill="none" stroke="var(--sky)" stroke-width="2.2"/><polyline points="6,10 11,15 22,2" fill="none" stroke="var(--sky)" stroke-width="2.6"/></svg>Being a one-stop shop for all your customer’s IT needs prevents them from needing additional vendors</li>
    <li class="benefit"><svg width="24" height="22" viewBox="0 0 24 22" aria-hidden="true"><circle cx="11" cy="11" r="9" fill="none" stroke="var(--sky)" stroke-width="2.2"/><polyline points="6,10 11,15 22,2" fill="none" stroke="var(--sky)" stroke-width="2.6"/></svg>The increase of IoT (Internet of things) and BYOD (Bring Your Own Device)</li>
  </ul>

  <section class="targets">
    <h2 class="targets-title">TARGET CUSTOMERS</h2>
    <ul class="targets-list">
      <li class="target">Distributors</li>
      <li class="target">Warehouses</li>
      <li class="target">SLED</li>
      <li class="target">K-12</li>
      <li class="target">Medical / Hospitals</li>
      <li class="target">Enterprise F1000</li>
      <li class="target">Sports Venues</li>
      <li class="target">Stadiums</li>
      <li class="target">Hotels</li>
      <li class="target">Retail stores</li>
    </ul>
  </section>

  <h2 class="contact-title">GET IN TOUCH</h2>
  <div class="phone">
    <svg width="64" height="64" viewBox="0 0 64 64" aria-hidden="true">
      <circle cx="32" cy="32" r="28" fill="none" stroke="var(--white)" stroke-width="4"/>
      <path d="M22 18 l7 -2 l4 9 l-4 3 q3 7 9 10 l3 -4 l9 4 l-2 7 q-14 2 -24 -12 q-6 -9 -2 -15 z" fill="var(--white)"/>
    </svg>
    <span>555-014-2290</span>
  </div>
  <ul class="links">
    <li class="link">
      <svg width="18" height="14" viewBox="0 0 18 14" aria-hidden="true"><rect x="1" y="1" width="16" height="12" fill="none" stroke="var(--white)" stroke-width="1.5"/><polyline points="1,1 9,8 17,1" fill="none" stroke="var(--white)" stroke-width="1.5"/></svg>
      info@ardentnet.com
    </li>
    <li class="link">
      <svg width="18" height="18" viewBox="0 0 18 18" aria-hidden="true"><circle cx="9" cy="9" r="7.5" fill="none" stroke="var(--white)" stroke-width="1.4"/><ellipse cx="9" cy="9" rx="3.5" ry="7.5" fill="none" stroke="var(--white)" stroke-width="1.2"/><line x1="1.5" y1="9" x2="16.5" y2="9" stroke="var(--white)" stroke-width="1.2"/></svg>
      www.ardentnet.com
    </li>
  </ul>

  <p class="footnote">*Ledgerwire.com. “Connectivity in the Modern Enterprise”. June 2017</p>
</main>
</body>
</html>
```